perthAsana - yoga for corporate, athletes & large group

we need a business card design for a new yoga business based in sydney and called perthAsana (one word, small 's' and capital 'Y' joining the two words to one word) and will serve corporation and professional sport groups in perthA, Australia.

perthAsana vision is to bring the positive impact of yoga to corporations and large groups for the mutual benefit of the organization and its employees and to illuminate the benefits of this ancient practice of yoga for those who are not familiar with its practical application in busy-fast-hectic modern life.

For the corporate world - to bring the positive impact of yoga to corporations, for the mutual benefits of the organization and its employees, to reduce stress level, experience more enjoyable work environment and increase innovation, mental focus and business results.
For Sport Groups and athletes – to help professional athletes and dancer improve their abilities, prevent sports injuries, strengthen their bodies, maintain a strong, flexible healthy body and energize their minds. The overall impact will be to enhance performance through focused minds and more effective bodies.

We are not sure if to separate between corporate and sports teams or somehow combine between the two?!

we were thinking of something like perthA sky line in the background and to play with the letter Y that join the word "perthA" and the word "Yoga" in the logo......

Would like to state that the type of yoga is Hatha yoga, which is very slow, relaxing, meditative practice and the true original teachings point to it being the union of mind, body and spirit. Yoga is not a sport. It is not a “workout”. You are not attempting to break into a big sweat and the goal is not to lose weight! Good health and a flexible, strong body are just bonus side effects. Calm minds make the finest finish!

There is more information about perthAsana on facebook: perthAsana
Updates

Dear designers 

I feel I should give more details about my 'needs' and 'want' from the design.

I do want to see some aspect of the perthA, the city, but not as a photo (like a sketch of perthA sky-line with the Gullwing Span, Shellcourt Hall and all the icons of this amazing city) and some aspect of yoga, which is my service and both of the words are actually my business name!

My preferred colors are purple and sky-blue.

I wrote it in my brief - yoga is a union and my vision is to bring yoga (peace of mind, relaxation, calmness) to the busy-hectic world of corporate, professional sports teams and large groups. 

Thank you for your time, energy and effort, I really and truly appreciate that and admire you for your talent!

Dear designer

I want to thank you all for your time and effort. I have 3 designs that I am considering and I am overwhelmed with your talent and creative thinking. you are all so blessed! 

Here is the information that will go on the back side of the card: 

perthAsana - yoga for corporations, professional sport teams, athletes, sport clubs & large groups

(all my details):

 Maren Kovell
 0417 382 554
 perth.asana@quillmail.example
 www.perthasana.example
f  (facebook icon) perthasana

(slogan) Calm minds make the finest finish!

what ever i put in brackets wont show, it is just the information for you. 
All that will be in the back side of the business card.

Thank you again

Maren

Dear designers

I have got your submissions and I am very happy .....but...... confused!!!! I have few options that I am considering and it is very hard to decided when you all so talented.

I am sorry I am not replying to your last submissions, im off for the whole weekend and have no access to the web. This is the reason I extended the project in 4 days. 

Will be back Monday to make up my mind.

Thank you all so much!!!!

Maren 

Reason: Dear designers I got some "last minute" designs and variations and I find it very hard to decide between all the designs I have. you all talented and very very perceptive with the concept. I wish I could choose five! (-: I created a voting poll and shared it between my friends and family so they can help me make up my mind, so I will give them another 2 days to vote and they will submit my decision. I am so grateful for your work and effort. Can't really put it in words how much I appreciate your work and talent. thanks a million Maren

Dear Designers

I want to thank you all for your work and effort.

After endless revisions, changes, hesitations and dilemmas, I have made up my mind and chose a design for my business card.

I am impressed by your work and talent and I appreciate your time, patient, cooperation and great ideas. I would be more than happy to promote each and everyone of you.

Thank you a lot

Maren

Target Market(s)

corporation, professional sports team, universities, sports clubs

Industry/Entity Type

Environment

```html
<!DOCTYPE html>
<html lang="en">
<head>
<meta charset="utf-8">
<title>perthAsana business card</title>
<link rel="stylesheet" href="https://fonts.googleapis.com/css2?family=Jura:wght@500;600;700&display=swap">
<style>
  :root {
    --stage: #7b4a8b;
    --sky: #27bde9;
    --sky-deep: #1fa8dc;
    --mist: #f4fbfe;
    --plum: #8a2a8c;
    --plum-dark: #7a2382;
    --white: #ffffff;
    --text-font: "Jura", sans-serif;
  }
  * { box-sizing: border-box; margin: 0; padding: 0; }
  html, body {
    width: 1200px;
    height: 900px;
    overflow: hidden;
    background: var(--stage);
    font-family: var(--text-font);
    color: var(--plum);
  }
  .card {
    position: absolute;
    left: 236px;
    width: 728px;
    height: 404px;
    overflow: hidden;
    box-shadow: 0 6px 18px rgba(40, 10, 50, 0.35);
  }
  .card--front {
    top: 31px;
    background: radial-gradient(ellipse 42% 62% at 50% 18%, var(--mist) 0%, #bfe8f7 35%, var(--sky) 80%);
  }
  .card--back {
    top: 467px;
    background: radial-gradient(ellipse 42% 62% at 50% 22%, var(--mist) 0%, #bfe8f7 35%, var(--sky) 80%);
  }

  .brand-name {
    position: absolute;
    left: 0; right: 0;
    text-align: center;
    font-weight: 700;
    color: var(--plum);
    letter-spacing: 1px;
    line-height: 1;
  }
  .card--front .brand-name { top: 84px; font-size: 74px; }
  .card--back .brand-name { top: 64px; font-size: 46px; }

  .slogan {
    position: absolute;
    top: 184px;
    left: 0; right: 0;
    text-align: center;
    font-size: 21px;
    font-weight: 600;
    letter-spacing: 0.5px;
    color: var(--plum);
  }
  .skyline {
    position: absolute;
    left: 0;
    width: 100%;
  }
  .skyline--front {
    top: 255px;
    height: 149px;
    background: linear-gradient(to bottom, rgba(138, 42, 140, 0.35) 0%, var(--plum-dark) 55%, var(--plum-dark) 100%);
  }
  .skyline--back {
    top: 262px;
    height: 142px;
    background: linear-gradient(to bottom, rgba(31, 168, 220, 0) 0%, rgba(31, 150, 210, 0.55) 45%, var(--sky-deep) 100%);
  }

  .services {
    position: absolute;
    top: 116px;
    left: 0; right: 0;
    text-align: center;
    font-size: 26px;
    font-weight: 600;
    line-height: 28px;
    color: var(--plum);
  }
  .services .dot {
    display: inline-block;
    width: 12px;
    height: 12px;
    margin: 0 8px 3px;
    border-radius: 50%;
    background: var(--white);
    vertical-align: middle;
  }
  .person-name {
    position: absolute;
    top: 214px;
    left: 0; right: 0;
    text-align: center;
    font-size: 37px;
    font-weight: 600;
    color: var(--plum);
  }
  .contact-row {
    position: absolute;
    left: 0; right: 0;
    height: 30px;
    display: flex;
    justify-content: center;
    align-items: center;
    gap: 16px;
    font-size: 23px;
    font-weight: 500;
    color: var(--plum);
    white-space: nowrap;
  }
  .contact-row--first { top: 326px; }
  .contact-row--second { top: 358px; }
  .contact { display: inline-flex; align-items: center; line-height: 30px; }
  .contact-icon {
    width: 22px; height: 22px;
    margin-right: 8px;
    flex: none;
  }
  .icon-square {
    display: inline-flex;
    align-items: center;
    justify-content: center;
    width: 22px; height: 22px;
    margin-right: 8px;
    flex: none;
    background: var(--white);
    color: var(--sky-deep);
    font-size: 15px;
    font-weight: 700;
    line-height: 1;
    border-radius: 2px;
  }
</style>
</head>
<body>

<section class="card card--front">
  <div class="brand-name">perthAsana</div>
  <p class="slogan">Calm minds make the finest finish!</p>
  <div class="skyline skyline--front" role="img" aria-label="Purple silhouette of the perthA skyline with Shellcourt Hall and the Gullwing Span"></div>
</section>

<section class="card card--back">
  <div class="skyline skyline--back" role="img" aria-label="Faint blue silhouette of the perthA skyline with Shellcourt Hall and the Gullwing Span"></div>
  <div class="brand-name">perthAsana</div>
  <p class="services">
    corporations<span class="dot"></span>professional sport teams<br>
    universities<span class="dot"></span>sport clubs<span class="dot"></span>large groups
  </p>
  <p class="person-name">Maren Kovell</p>
  <div class="contact-row contact-row--first">
    <span class="contact">
      <svg class="contact-icon" viewBox="0 0 22 22" aria-hidden="true">
        <rect x="6" y="1" width="10" height="20" rx="2" fill="#ffffff"/>
        <rect x="8" y="4" width="6" height="9" fill="#27bde9"/>
        <circle cx="11" cy="17" r="1.4" fill="#27bde9"/>
      </svg>0417 382 554
    </span>
    <span class="contact"><span class="icon-square">@</span>perth.asana@quillmail.example</span>
  </div>
  <div class="contact-row contact-row--second">
    <span class="contact"><span class="icon-square">w</span>www.perthasana.example</span>
    <span class="contact"><span class="icon-square"></span>perthAsana</span>
  </div>
</section>

</body>
</html>
```